Paws of Kindness Care & Dog Training

I have a dual themed business. I am a nationally recognized dog trainer for NCR (National Canine Registry) and Gentle Tails (Pet Therapy). One side of my business card will need to address my pet therapy ministry called "Paws of Kindness Care". We visit almost 1,000 people a month bringing emotionally uplifting happy visits for nursing homes, veterans hospitals, hospice care, surgery recovery, school systems, and libraries, etc. In addition to emotionally positive effects, pet therapy also helps with anxiety, mobility, regulating blood pressure, and many more advantages. I've attached 2 graphics that are connected with this ministry; #1 paw print inside ribbon heart, #2 clasping hands sketch. The story behind the clasping hands is that it is an actual picture of my hand holding my mother's hand on her death bed (with a sketch filter used). My mother lived in a different state than I live in, and I had wished she had pet therapy available to her in her last months of life. They would have provided some bright moments to her difficult days. So, I vowed that although I was not able to help my own mother, I could train my own dog to reach out to hundreds of people in the community I live in. I have continued to live up to that vow, and have gone on to become a national trainer for other people who would like to train their pets to do the same thing.SIDE TWO of my business card will be announcing that I am a dog trainer for puppies, basic obedience, pet therapy, ESA (emotional support animals), and service dogs. Additionally, I offer canine body language training, dog agility training, and cognitive training. I have also attached two graphics for this side: #1 NCR logo, #2 Gentle Tails Evaluation

Industry/Entity Type

Dog Training

Contact Information for Business Card

I'm looking for a designer who is good with color scheme & fonts.
2-sided card
one side for pet therapy
one side for dog training

Logo Text

Paws of KindnessCare

Font styles to use
Sans Serif
Decorative

Colors

Designer to choose colors to be used in the design.

Requirements
Must have
• -Contact information: Marcy Dunwell (555) 274-9316
• - Contact information for online: Paws of Kindness Care (Facebook, Instagram & Twitter)
• - Graphics for pet therapy: clasping hands
• - Graphics for dog training: NCR Model Hound Award, Gentle Tails
• - List of dog training classes I offer: Basic Obedience, NCR Model Hound Award, NCR B.R.I.G.H.T. Pup, Pet Therapy training, ESA (Emotional Support Animal), Service Dog training, Canine Body Language, Dog Agility, Cognitive Training, Dog Trick Training
Nice to have
• appealing graphic for dog training school
• Titles in decorative font (but still easy to read) & detail info in very easy to read font

```html
<!DOCTYPE html>
<html lang="en">
<head>
<meta charset="utf-8">
<title>Paws of Kindness Care – Business Card</title>
<link href="https://fonts.googleapis.com/css2?family=Montserrat:wght@700;800&family=Open+Sans:wght@400;600&family=Oswald:wght@700&display=swap" rel="stylesheet">
<style>
  :root {
    --stage: #2a2b2e;
    --navy-deep: #0d1330;
    --navy: #1c2660;
    --navy-soft: #2a3577;
    --green: #1fa94f;
    --green-bright: #2dbb5c;
    --white: #ffffff;
    --muted: #d9dcea;
    --sketch-light: #c8a878;
    --sketch-dark: #5a3a22;
  }
  * { margin: 0; padding: 0; box-sizing: border-box; }
  html, body { width: 1200px; height: 960px; overflow: hidden; }
  body {
    background: var(--stage);
    position: relative;
    font-family: "Open Sans", sans-serif;
  }
  .card {
    position: absolute;
    left: 220px;
    width: 760px;
    height: 434px;
    border-radius: 22px;
    overflow: hidden;
    background: linear-gradient(135deg, var(--navy-soft), var(--navy) 45%, var(--navy-deep));
  }
  .card--front { top: 24px; }
  .card--back { top: 502px; }

  .photo-backdrop {
    position: absolute; inset: 0;
    background: radial-gradient(ellipse at 55% 40%, rgba(90,100,160,.35), rgba(13,19,48,0) 70%);
  }

  /* front */
  .brand {
    position: absolute; left: 60px; top: 70px;
    display: flex; align-items: center; gap: 12px;
  }
  .brand__dot { width: 34px; height: 34px; border-radius: 50%; background: var(--green); }
  .brand__name {
    font-family: "Montserrat", sans-serif; font-weight: 800;
    color: var(--white); font-size: 26px; line-height: 1.15; width: 190px;
  }
  .divider { position: absolute; left: 300px; top: 60px; }
  .contact {
    position: absolute; left: 400px; top: 96px;
  }
  .contact__name {
    font-family: "Montserrat", sans-serif; font-weight: 800;
    color: var(--green-bright); font-size: 44px; letter-spacing: .5px; margin-bottom: 14px;
  }
  .contact__row {
    display: flex; align-items: center; gap: 12px;
    color: var(--muted); font-size: 19px; line-height: 30px;
  }
  .contact__row svg { width: 18px; height: 18px; flex: none; }

  .band {
    position: absolute; left: 0; right: 0; bottom: 0; height: 92px;
    background: var(--green);
    display: flex; align-items: center; padding-left: 30px; gap: 16px;
  }
  .band__social { display: flex; gap: 10px; }
  .band__social span { width: 32px; height: 32px; border-radius: 50%; background: var(--white); opacity: .9; }
  .band__tagline {
    font-family: "Montserrat", sans-serif; font-weight: 700;
    color: var(--white); font-size: 26px; margin-left: 14px;
  }
  .hands {
    position: absolute; right: 0; bottom: 0; width: 230px; height: 170px;
    background: radial-gradient(ellipse at 45% 50%, var(--sketch-light), var(--sketch-dark) 75%, rgba(90,58,34,0) 100%);
    opacity: .9;
  }

  /* back */
  .classes {
    position: absolute; inset: 0;
    display: flex; flex-direction: column; justify-content: center; align-items: center;
    font-family: "Oswald", sans-serif; font-weight: 700;
    color: var(--white); font-size: 29px; line-height: 1.5; text-align: center;
    text-shadow: 0 2px 4px rgba(0,0,0,.5);
  }
</style>
</head>
<body>

<section class="card card--front">
  <div class="photo-backdrop" role="img" aria-label="Dimmed photo of a therapy visit with a person and dog, tinted navy"></div>

  <div class="brand">
    <span class="brand__dot"></span>
    <span class="brand__name">Tailwise Dog School</span>
  </div>

  <svg class="divider" width="90" height="180" viewBox="0 0 90 180">
    <line x1="88" y1="2" x2="2" y2="178" stroke="#ffffff" stroke-width="1.5" opacity=".8"/>
  </svg>

  <div class="contact">
    <div class="contact__name">Marcy Dunwell</div>
    <div class="contact__row">
      <svg viewBox="0 0 24 24"><path d="M6 2h4l2 5-3 2a11 11 0 0 0 6 6l2-3 5 2v4a2 2 0 0 1-2 2A18 18 0 0 1 4 4a2 2 0 0 1 2-2z" fill="#fff"/></svg>
      (555) 274-9316
    </div>
    <div class="contact__row">
      <svg viewBox="0 0 24 24"><rect x="2" y="5" width="20" height="14" fill="none" stroke="#fff" stroke-width="2"/><path d="M2 5l10 8 10-8" fill="none" stroke="#fff" stroke-width="2"/></svg>
      marcy@kindpaws.net
    </div>
    <div class="contact__row">
      <svg viewBox="0 0 24 24"><circle cx="12" cy="12" r="9" fill="none" stroke="#fff" stroke-width="2"/><path d="M3 12h18M12 3c3 3 3 15 0 18M12 3c-3 3-3 15 0 18" fill="none" stroke="#fff" stroke-width="1.5"/></svg>
      www.kindpawscare.com
    </div>
  </div>

  <div class="band">
    <div class="band__social"><span></span><span></span><span></span></div>
    <div class="band__tagline">Paws of Kindness Care</div>
  </div>

  <div class="hands" role="img" aria-label="Sketch of two clasped hands with a paw print ribbon heart"></div>
</section>

<section class="card card--back">
  <div class="photo-backdrop" role="img" aria-label="Dimmed photo of a dog training session, tinted navy"></div>
  <div class="classes">
    <p>Basic Obedience, NCR Model Hound Award</p>
    <p>NCR B.R.I.G.H.T. Pup, Pet Therapy training</p>
    <p>ESA (Emotional Support Animal), Service Dog training</p>
    <p>Canine Body Language, Dog Agility</p>
    <p>Cognitive Training, Dog Trick Training</p>
  </div>
</section>

</body>
</html>
```